[Green Press + Juice Bar] Digital Menu Boards (2)

We need designs for our digital menu screens. Dimensions are 1080 x 1920 (9:16). Screens are in portrait mode–2 of them. They will be side by side so designs should be cohesive. We'll need the (Adobe) source files to be able to easily edit in the future.

Check out our Instagram (@pulpwell) to see current brand imagery for inspiration. Please disregard our current website design as it shows our old branding. Visit our Tastemap page to get a feel of the store flow in which the menu boards will be displayed: https://www.tastemap.example/biz/pulpwell-chicago-6

See "Larkfield Menu" attachment for content that will be incorporated into the design for 2 screens.

See "Cleanse Brochure" attachment to see current material we are using to promote our cleansing program. We would like to designate a portion of our menu to promote cleanse options, depending on how much room is available.

Also attached is a photo of our current, static menu board.

We've attached photos of color palettes we like.

Target Market(s)

Health-conscious individuals, healthy moms, fitness gurus, professionals

Industry/Entity Type

Health And Wellness

Font styles to use
Serif
Sans Serif

Colors

Designer to choose colors to be used in the design.

Requirements
Must have
• We need designs for our digital menu screens. Dimensions are 1080 x 1920 (9:16). Screens are in portrait mode–2 of them. We'll need the (Adobe) source files to be able to easily edit in the future. To ensure the sizing of the outputted file is correct and spaced correctly, send us a test file to test on our TV.
Nice to have
• Ideally, the menu will reflect current branding with font usage of one or more of the following:
• FuturaStd-Bold
• Desiderata-Regular
• Wisdom Script
• Bernier Typeface
• Swistblnk Banthers
• Hanley
• If there is space, we'd like to have space to roll a photo/video slideshow on the menu.

```html
<!DOCTYPE html>
<html lang="en">
<head>
<meta charset="utf-8">
<title>Green Press + Juice Bar — Larkfield Menu Boards</title>
<link href="https://fonts.googleapis.com/css2?family=Jost:wght@400;500&family=Lobster&display=swap" rel="stylesheet">
<style>
  :root {
    --page: #f2f2f2;
    --board: #0b0b0b;
    --ink: #ffffff;
    --ink-soft: #e8e8e8;
  }
  * { margin: 0; padding: 0; box-sizing: border-box; }
  html, body { width: 1200px; height: 1104px; overflow: hidden; background: var(--page); }
  body { position: relative; font-family: "Jost", sans-serif; color: var(--ink); }

  .board { position: absolute; top: 18px; height: 1067px; background: var(--board); }
  .board--drinks { left: 8px; width: 584px; }
  .board--food { left: 608px; width: 583px; }

  .section-title {
    position: absolute; left: 0; right: 0; text-align: center;
    font-family: "Lobster", cursive; font-weight: 400; line-height: 1;
  }
  .section-title small {
    font-family: "Jost", sans-serif; font-size: 13px; letter-spacing: 1.5px; margin-left: 4px;
  }
  .board--drinks .section-title { font-size: 50px; }
  .board--food .section-title { font-size: 40px; }

  .item { position: absolute; white-space: nowrap; }
  .item-name { text-decoration: underline; text-decoration-thickness: 1px; text-underline-offset: 3px; }

  .smoothie { left: 28px; }
  .smoothie h3 { font-weight: 400; font-size: 24px; letter-spacing: 3.6px; line-height: 26px; }
  .smoothie p { font-size: 14px; letter-spacing: 3px; line-height: 16.6px; color: var(--ink-soft); }
  .smoothie .steps { margin-top: 18px; }

  .food h3 { font-weight: 400; font-size: 16.5px; letter-spacing: 1.95px; line-height: 19px; }
  .food p { font-size: 12.2px; letter-spacing: 1.7px; line-height: 13.8px; color: var(--ink-soft); }
  .food p + p { margin-top: 13px; }
  .bowl h3 { font-size: 18px; letter-spacing: 2.4px; }
  .bowl p { font-size: 13px; letter-spacing: 2px; }

  .photo { position: absolute; }
  .photo--glasses { left: 23px; top: 940px; width: 169px; height: 115px; background: linear-gradient(90deg, #c9574a, #8fa845 50%, #e1a43a); }
  .photo--pink { left: 206px; top: 940px; width: 170px; height: 115px; background: linear-gradient(90deg, #f2b7b8, #f7f4ee 55%, #c8d77a); }
  .photo--jar { left: 390px; top: 940px; width: 170px; height: 115px; background: linear-gradient(135deg, #2a2d33, #7d2630 55%, #22252a); }
  .photo--bowl { left: 345px; top: 401px; width: 221px; height: 153px; background: linear-gradient(135deg, #e9e9e7, #d9c7b0 50%, #ecebe8); }

  .cleanse { left: 13px; top: 995px; }
  .cleanse p { font-size: 12.2px; letter-spacing: 2.3px; line-height: 14px; color: var(--ink-soft); }
  .cleanse-title { font-size: 31px !important; }
</style>
</head>
<body>

<section class="board board--drinks">
  <h2 class="section-title" style="top:34px">Smoothies<small>(18 oz)</small></h2>

  <div class="item smoothie" style="top:104px">
    <h3><span class="item-name">Midnight Heron</span> - 10.5</h3>
    <p>Housemade Almond Milk, HillBrew Coffee,<br>Banana, Coconut Meat, Raw Cacao, Medjool<br>Dates, Tocotrienols, Maca topped with Raw Cacao<br>Drizzle and Housemade Coconut Whip</p>
  </div>
  <div class="item smoothie" style="top:213px">
    <h3><span class="item-name">Green Willow</span> - 11</h3>
    <p>Housemade Almond Milk, Banana, Avocado, Spinach,<br>Sprouted Almond Butter, Verdant Greens, Maca,<br>Moringa, Medjool Dates, Tocotrienols</p>
  </div>
  <div class="item smoothie" style="top:304px">
    <h3><span class="item-name">Jade Garden</span> - 10</h3>
    <p>Housemade Almond milk, Banana, Avocado, Pineapple,<br>Spinach, Matcha, Spirulina, Mint,Tocotrienols,<br>Local Honey, Pink Salt (Upgrade: Verdant Greens, +1)</p>
  </div>
  <div class="item smoothie" style="top:396px">
    <h3><span class="item-name">Blue Harvest</span> - 10</h3>
    <p>Housemade Almond Milk, Banana, Blueberries, Peanut<br>Butter, Medjool Dates, Tocotrienols,Lucuma, Pink Salt</p>
  </div>
  <div class="item smoothie" style="top:471px">
    <h3><span class="item-name">Cherry Maca Power</span>- 10.5</h3>
    <p>Fresh-cracked Coconut Water, Cherries, Banana,<br>Peanut Butter, Vegan Mocha Protein Powder,Maca</p>
  </div>
  <div class="item smoothie" style="top:546px">
    <h3><span class="item-name">Ember Crush</span> - 10</h3>
    <p>Fresh-cracked Coconut Water, Apple Juice, Coconut Meat,<br>Banana, Mango, Pineapple, Strawberry, Tocotrienols,<br>Camu Camu, Hemp Seeds, Jalapeno</p>
  </div>
  <div class="item smoothie" style="top:638px">
    <h3><span class="item-name">Frosted Mint</span> - 10.5 (seasonal)</h3>
    <p>Almond Milk, Banana, Cherries, Raw Cacao Drizzle,<br>Sprouted Almond Butter, Tocotrienols, Dates, Peppermint,<br>Pink Salt. Topped with Raw Cacao Drizzle, Cacao Nibs,<br>Mint and Housemade Coconut Whip</p>
  </div>
  <div class="item smoothie" style="top:747px">
    <h3><span class="item-name">Build Your Own Smoothie</span> - 10.5</h3>
    <p class="steps">Step 1: Start with Your Liquid:<br>Housemade Almond Milk, Apple Juice, or Coconut Water<br>Step 2: Add Your Base:<br>Avocado, Banana, or Coconut Meat<br>Step 3: Choose up to 3 fruits or veggies<br>Step 4: Choose up to 2 Superfoods<br>Step 5: Choose a Sweetener:<br>Medjool Dates, Local Honey, Xylitol</p>
  </div>

  <div class="photo photo--glasses" role="img" aria-label="Photo of rows of colourful juice glasses"></div>
  <div class="photo photo--pink" role="img" aria-label="Photo of strawberry and kiwi smoothies with straws"></div>
  <div class="photo photo--jar" role="img" aria-label="Photo of a berry smoothie in a mason jar"></div>
</section>

<section class="board board--food">
  <h2 class="section-title" style="top:20px">Bowls<small>(20 oz)</small></h2>

  <div class="item food bowl" style="left:18px; top:72px">
    <h3><span class="item-name">Matcha Bowl</span> - 12.5</h3>
    <p>Base: Fresh-cracked Coconut<br>Water, Coconut Meat, Banana,<br>Spinach, Medjool Dates,<br>Tocotrienols, Maca, Matcha,<br>Spirulina</p>
    <p>Toppings: Hemp Seeds,<br>Blueberries, Cacao Nibs, Coconut<br>Shreds, Kiwi, Pomegranate Seeds,<br>Banana, Bee Pollen, Mint Sprig</p>
  </div>
  <div class="item food bowl" style="left:18px; top:241px">
    <h3><span class="item-name">Berry Sunrise</span> - 12</h3>
    <p>Base: Acai, Fresh-pressed Apple<br>Juice, Cherries, Banana,<br>Strawberry, Pomegranate,</p>
    <p>Toppings: Seasonal Berries,<br>Banana, Sprouted Almond Butter,<br>Coconut Shreds, Goji Berries,<br>Bee Pollen, Housemade Coconut<br>Whip, Housemade Raw Granola,<br>Local Honey</p>
  </div>
  <div class="item food bowl" style="left:295px; top:72px">
    <h3><span class="item-name">Painted Orchard</span> - 12</h3>
    <p>Base: Acai, Housemade Almond<br>Milk, Bananas, Blueberries,<br>Peanut Butter, Medjool Dates</p>
    <p>Toppings: Housemade Raw Granola,<br>Raw Chocolate Hearts, Peanut<br>Butter, Raw Cacao Drizzle, Banana,<br>Dried Banana Chips, Cacao Nibs,<br>Local Honey, Bee Pollen</p>
  </div>
  <div class="item food bowl" style="left:295px; top:228px">
    <h3><span class="item-name">Keto Bowl</span> - 13<br>(under 15 net carbs)</h3>
    <p>Base: Acai, Housemade Almond Milk,<br>Coconut Meat, Avocado, Blueberries,<br>Cauliflower, Pineapple, Sprouted<br>Almond Butter, Xylitol</p>
    <p>Toppings: Seasonal Berries,<br>Coconut Shreds, Bee Pollen,<br>Hemp Seeds, Mulberries, Chia<br>Seeds</p>
  </div>
  <div class="item food" style="left:16px; top:408px">
    <h3 style="font-size:18px; letter-spacing:2.4px"><span class="item-name">Build Your Own Bowl</span> - 12.5</h3>
    <p>Step 1: Start with Your Liquid:<br>Almond Milk, Apple Juice, Coconut Water<br>Step 2: Choose up to 2 fruits or veggies<br>(all bowls include banana)<br>Step 3: Choose up to 2 Superfood Add-ins<br>Step 4: Choose up to 4 Superfood Toppings<br>Step 5: Choose a Sweetener:<br>Medjool Dates, Local Honey, Xylitol</p>
  </div>
  <div class="photo photo--bowl" role="img" aria-label="Photo of a yogurt bowl with granola and berries"></div>

  <h2 class="section-title" style="top:552px">Bites</h2>
  <div class="item food" style="left:13px; top:601px">
    <h3><span class="item-name">Hot Oatmeal + Seasonal Fruit + Superfood Toppings</span> - 7.5<br>(served until 10:30am)</h3>
  </div>
  <div class="item food" style="left:13px; top:648px">
    <h3><span class="item-name">Avocado Toast</span> - 8.5 for 2 slices 8.5 / 4.5 for 1 slice</h3>
    <p>Sprouted Seven-Grain Bread, Avocado, Pomegranate, Fig, Rosemary</p>
  </div>
  <div class="item food" style="left:13px; top:693px">
    <h3><span class="item-name">Orange Cacao Toast</span>- 8.5 for 2 slices / 4.5 for 1 slice<br>(seasonal)</h3>
    <p>Sprouted Cinnamon Raisin Loaf, Sprouted Almond Butter,<br>Orange, Cacao Nibs, Local Honey, Basil</p>
  </div>

  <h2 class="section-title" style="top:771px">Soups</h2>
  <div class="item food" style="left:13px; top:825px">
    <h3><span class="item-name">Broccoli “Cheddar” Soup</span> - 16oz (Dairy Free)</h3>
    <p>Red Pepper, Carrot, Cashew, Spring Onion, Lemon, Maple, Nutritional<br>Yeast, Pink Salt, Chili Powder, Garlic Powder, Broccoli</p>
  </div>
  <div class="item food" style="left:13px; top:882px">
    <h3><span class="item-name">Veggie Soup with Sprouted Lentil</span> - 16oz</h3>
    <p>Leek, Kale, Celery, Red Pepper, Green Onion, Liquid Aminos,<br>Fresh Ginger, Fresh Garlic, Lemon, Salt, Pepper, Cumin,<br>Turmeric, Sprouted Lentils</p>
  </div>

  <h2 class="section-title cleanse-title" style="top:950px">Signature Juice and Smoothie Cleanses</h2>
  <div class="item cleanse">
    <p>- Available at 65/day with nationwide delivery.<br>- Choose from 5 different signature cleanses in 1, 3, 5 or 7-day packages<br>- Reboot your body by providing a digestive vacation while refocusing<br>&nbsp;&nbsp;the mind.</p>
  </div>
</section>

</body>
</html>
```